Event Listing Website

We need a redesign of a site for a new startup that lists local events such as concerts, night clubs, stand up comedy shows, theater plays, festivals, conferences, seminars, and family events.

The original design was done by programmers, not designers, and thus can be greatly improved, especially in terms of flow and usability.

The current site can be viewed at:
http://projects.brinvexsystems.example/pellora/index.php/events/

The successful designer may also be hired for additional work. In fact, we are looking for a long-time partner that may eventually fill a Creative Director role with this new venture..

Things to note:

The site should not look like a nightlife/disco/club site since the site lists events from concerts to conferences to family events.

There is a lot of content on the site, thus it needs to be clean, easy to read and navigate.

Our mission is to have a “Unique” site, that stands out from the traditional ones

Currently the site has these main sections:

Homepage
Events
Venues
Cinema

These sections have the following content types or page layouts:

Homepage
Listing of events
Listing of venues
Event details
Venue details
Cinema summary page
Film details
Film theater details
Blog/news
Account overview page
Updates

Please note, an important element of the site is the location picker that is currently on the top left of our site (the black drop down button that says "change", enter Roma for example). The site displays events based on user location, users need to know what city the site is using and need to be able to change such city. This works similar to many sites such as www.dealnorva.example, www.partyvesk.example, and www.happenlo.example.

Also, please note that we would eventually use background ads on the homepage. See www.ticketmurn.example for example.

I have extended the project further. Thanks!

Please note, after the main menu (Home, Events, Venues, Cinema) these pages or features are very important and should be visible and prominent. We currently have them on a bar across the top that remains fixed as you scroll down, but it may not be the best location, so we look forward to some fresh ideas. Thanks.

In order of importance:

1. Change your location (Button that says current city with option to change it)
2. Add event (link)
3. Add venue (link)
4. Login (link)
5. Change language (drop down button with languages)

I just increased the budget by $40 :)

When submitting a design, please submit two versions, one with background advertisement, and one without. This way we can see if there are too many colors or distractions.

Here is a sample background advertisement to use: http://lentobanner.example/img_uploads/72/77_191072_3_Korvex_Viola_Tab_Adriva_newsln_skin2.jpg

Hello all, thanks for submitting your beautiful designs. It has made our decision very difficult. We decided to award to project to Merostin, who is currently working on making some tweaks to his submission. Thus are no longer accepting designs. Thanks again.

Target Market(s)

17-40 year olds, male and female, clubbers, concert goers, professionals, athletes, families, and kids

Industry/Entity Type

Events

Requirements
Must have
• Needs to follow 960 grid system. See http://gridlane.example.
Nice to have
• We like the colors Bravik Nearby
(http://nearby.bravik.example/westside-south-bay)

We like Dealnorva theme as well
(http://www.dealnorva.example/los-angeles/)

Happenlo is a site similar to ours, we like the overall layout and how easy it is to navigate, not necessarily the colors though:
(http://happenlo.example/)
Should not have
• The site should not look like a nightlife/disco/club site.

Besides clubs, the site lists events from concerts to conferences to family events.

Should definitely not use serif fonts such as Times New Roman

```html
<!DOCTYPE html>
<html lang="en">
<head>
<meta charset="utf-8">
<title>Pellora – National Park venue</title>
<link href="https://fonts.googleapis.com/css2?family=Ubuntu:wght@400;500;700&display=swap" rel="stylesheet">
<style>
:root{
  --page:#f1f1ef;
  --blue:#12a5dc;
  --blue-dark:#0c8fc2;
  --orange:#e2540d;
  --green:#8dc63f;
  --ink:#333;
  --muted:#777;
  --bar:#3b3b3b;
  --panel:#fff;
  --soft:#f3f3f3;
  --line:#dcdcdc;
  --footer:#222;
  --footer-text:#8a8a8a;
}
*{box-sizing:border-box;margin:0;padding:0}
html,body{width:994px;height:1200px;overflow:hidden}
body{background:var(--page);font-family:"Ubuntu",sans-serif;color:var(--ink);position:relative;font-size:10px}
a{color:inherit;text-decoration:none}
.abs{position:absolute}

/* header */
.site-header{left:108px;top:65px;width:780px;height:64px;background:var(--blue);color:#fff}
.logo{left:15px;top:14px;font-size:30px;font-weight:400;letter-spacing:.3px}
.main-nav .item{position:absolute;top:0;height:64px;width:66px;text-align:center;font-size:13px;padding-top:10px}
.main-nav .item svg{display:block;margin:0 auto 5px}
.main-nav .active{background:var(--orange)}
.search{left:601px;top:25px;width:164px;height:22px;border:1px solid #fff;font-size:11px;padding:4px 6px}
.search svg{position:absolute;right:6px;top:4px}

.sub-bar{left:108px;top:129px;width:780px;height:33px;background:var(--blue-dark);color:#fff;font-size:13px}
.sub-bar .abs{top:8px}
.city-pick{background:var(--orange);padding:1px 5px;font-weight:700}
.plus{display:inline-block;width:14px;height:11px;background:var(--orange);vertical-align:middle;margin-left:4px;position:relative}
.plus::before,.plus::after{content:"";position:absolute;background:#fff;left:5px;top:2px;width:3px;height:7px}
.plus::after{left:3px;top:4px;width:7px;height:3px}
.lang{left:710px;top:5px!important;width:55px;height:22px;background:var(--blue);padding:3px 6px}

/* main column */
.section-title{left:108px;top:178px;width:514px;height:21px;background:var(--blue);color:#fff;font-size:14px;padding:2px 13px}
.crumbs{left:108px;top:200px;width:514px;height:34px;background:var(--bar);color:#fff;font-size:10px;padding:11px 13px}
.crumbs .promote{position:absolute;right:12px;top:11px}
.gtick{color:var(--green);font-weight:700}
.venue-panel{left:108px;top:234px;width:514px;height:569px;background:var(--panel)}

.share-box{left:50px;top:234px;width:56px;height:164px;background:#fff}
.share{position:absolute;left:6px;width:43px;text-align:center}
.share .count{border:1px solid var(--line);height:22px;font-size:12px;padding-top:4px;color:#555}
.share .btn{margin-top:2px;height:15px;border:1px solid #c9d3de;background:#eef2f6;font-size:9px;color:#3b5a80;padding-top:1px}

.photo{left:123px;top:249px;width:163px;height:164px;border:1px solid var(--line);padding:5px;background:#fff}
.photo div{width:100%;height:100%;background:linear-gradient(180deg,#c9a16a 0%,#b98a4e 40%,#6d5a3c 70%,#3f3a2a 100%)}
.venue-name{left:301px;top:257px;font-size:14px;font-weight:700}
.addr{left:301px;top:292px;font-size:9px;line-height:16px;color:#555}
.rule{height:1px;background:var(--line)}
.directions{left:530px;top:294px;font-size:9px}
.venue-actions{left:301px;top:404px;font-size:9px}
.mini-ico{display:inline-block;width:9px;height:8px;background:var(--green);vertical-align:middle;margin-left:3px}

.description{left:123px;top:430px;width:483px;height:85px;background:var(--soft);padding:12px 13px;font-size:10px;line-height:16px;color:#444}
.description h3{font-size:11px;color:#222;margin-bottom:3px}

.bar-head{height:23px;background:var(--blue);color:#fff;font-size:12px;padding:4px 13px}
.bar-head .right{position:absolute;right:12px;top:5px;font-size:10px}
.events-table{left:123px;top:528px;width:483px}
.events-table .cols{height:23px;font-size:8px;color:#666;position:relative}
.events-table .row{height:28px;position:relative;font-size:9px;color:#444}
.row.alt,.row.first{background:var(--soft)}
.c{position:absolute;top:9px}
.buy{position:absolute;right:7px;top:8px;width:73px;height:13px;background:var(--orange);color:#fff;font-size:6px;font-weight:700;text-align:center;padding-top:3px}

.comments{left:123px;top:669px;width:483px}
.comment-box{height:80px;background:var(--soft);position:relative;margin-top:5px}
.avatar{position:absolute;left:7px;top:6px;width:42px;height:42px;background:linear-gradient(160deg,#d8d2c4,#5a5346)}
.comment-input{position:absolute;left:60px;top:12px;width:413px;height:30px;border:1px solid #b9c3cf;background:#fff;font-size:9px;padding:5px;color:#666}
.post-check{position:absolute;left:57px;top:52px;font-size:8px;color:#333}
.post-check i{display:inline-block;width:9px;height:9px;border:1px solid #666;vertical-align:middle;margin-right:3px}
.posting-as{position:absolute;left:262px;top:53px;font-size:8px;color:#555}
.posting-as b{color:#3b5a99;font-weight:400}
.comment-btn{position:absolute;right:10px;top:48px;width:56px;height:18px;background:#5f78ab;border:1px solid #29447e;color:#fff;font-size:9px;font-weight:700;text-align:center;padding-top:3px}
.plugin{left:125px;top:783px;font-size:7px;color:#555}
.plugin i{display:inline-block;width:10px;height:10px;background:#3b5a99;vertical-align:middle;margin-right:4px}

.newsletter{left:108px;top:813px;width:514px;height:53px;background:#fff}
.newsletter p{position:absolute;left:15px;top:14px;font-size:11px;font-weight:700;line-height:13px}
.newsletter p b{color:var(--green)}
.newsletter .field{position:absolute;left:180px;top:13px;width:246px;height:31px;border:1px solid #bbb;font-size:9px;color:#888;padding:10px 6px}
.newsletter .send{position:absolute;left:429px;top:13px;width:70px;height:31px;background:var(--orange);color:#fff;font-size:11px;text-align:center;padding-top:8px}

/* side column */
.map-panel{left:637px;top:172px;width:251px;height:246px;background:#fff}
.map{position:absolute;left:14px;top:15px;width:220px;height:216px;background:linear-gradient(135deg,#ece7d6,#dfe8c9 45%,#ecd9b8 70%,#e6e2d4)}
.ad{left:636px;top:425px;width:252px;height:209px;background:radial-gradient(circle at 55% 45%,#dff27a 0%,#8ed21e 45%,#4ea30f 100%)}

/* footer */
.site-footer{left:108px;top:873px;width:780px;height:327px;background:var(--footer);color:var(--footer-text)}
.social{position:absolute;left:14px;top:12px;display:flex;gap:0}
.social span{width:38px;height:26px;border-right:1px solid #3a3a3a;display:flex;align-items:center;justify-content:center}
.social span i{display:block;width:16px;height:16px;background:#e8e8e8}
.foot-rule{position:absolute;left:0;width:780px;height:1px;background:#3a3a3a}
.col{position:absolute;top:57px;font-size:10px;line-height:16.3px}
.col h4{color:#fff;font-size:12px;font-weight:400;margin-bottom:14px}
.col .in{padding-left:16px}
.vsep{position:absolute;top:60px;width:1px;height:143px;background:#3a3a3a}
.copyright{position:absolute;left:149px;top:268px;font-size:11px;line-height:15px}
.copyright b{color:#fff;font-weight:400}
</style>
</head>
<body>

<header class="abs site-header">
  <div class="abs logo">Pellora</div>
  <nav class="main-nav">
    <a class="item" style="left:180px">
      <svg width="22" height="20" viewBox="0 0 22 20"><path d="M11 1 1 10h3v9h5v-6h4v6h5v-9h3z" fill="#fff"/></svg>Home</a>
    <a class="item active" style="left:257px">
      <svg width="22" height="20" viewBox="0 0 22 20"><rect x="1" y="6" width="20" height="13" rx="2" fill="#fff"/><rect x="7" y="2" width="8" height="5" rx="1" fill="none" stroke="#fff" stroke-width="2"/></svg>Events</a>
    <a class="item" style="left:330px">
      <svg width="22" height="20" viewBox="0 0 22 20"><path d="M11 0a7 7 0 0 0-7 7c0 5 7 13 7 13s7-8 7-13a7 7 0 0 0-7-7zm0 10a3 3 0 1 1 0-6 3 3 0 0 1 0 6z" fill="#fff"/></svg>Venues</a>
    <a class="item" style="left:408px">
      <svg width="22" height="20" viewBox="0 0 22 20"><rect x="4" y="1" width="14" height="18" fill="#fff"/><g fill="#12a5dc"><rect x="5" y="3" width="2" height="2"/><rect x="5" y="9" width="2" height="2"/><rect x="5" y="15" width="2" height="2"/><rect x="15" y="3" width="2" height="2"/><rect x="15" y="9" width="2" height="2"/><rect x="15" y="15" width="2" height="2"/><rect x="8" y="3" width="6" height="6"/><rect x="8" y="11" width="6" height="6"/></g></svg>Cinema</a>
  </nav>
  <div class="abs search">Search...
    <svg width="12" height="12" viewBox="0 0 12 12"><circle cx="5" cy="5" r="3.5" fill="none" stroke="#fff" stroke-width="1.6"/><path d="M7.5 7.5 11 11" stroke="#fff" stroke-width="1.8"/></svg>
  </div>
</header>

<div class="abs sub-bar">
  <div class="abs" style="left:15px">City: <span class="city-pick">Roma ▼</span></div>
  <div class="abs" style="left:183px">Add event<span class="plus"></span></div>
  <div class="abs" style="left:290px">Add venue<span class="plus"></span></div>
  <div class="abs" style="left:526px"><svg width="10" height="11" viewBox="0 0 10 11" style="vertical-align:-1px"><rect x="1" y="5" width="8" height="6" fill="#fff"/><path d="M3 5V3a2 2 0 0 1 4 0v2" fill="none" stroke="#fff" stroke-width="1.5"/></svg> Log in / Sing up</div>
  <div class="abs lang">Eng ▼</div>
</div>

<main>
  <h2 class="abs section-title">Venues</h2>
  <div class="abs crumbs">Home &gt; Events &gt; Santa Monica &gt; Venue &gt; National Park
    <span class="promote">Promote venue <span class="gtick">+</span></span></div>

  <section class="abs venue-panel"></section>

  <aside class="abs share-box">
    <div class="share" style="top:8px"><div class="count">163</div><div class="btn">Like</div></div>
    <div class="share" style="top:57px"><div class="count">919</div><div class="btn">Share</div></div>
    <div class="share" style="top:106px"><div class="count">25</div><div class="btn" style="color:#c33">+1</div></div>
  </aside>

  <div class="abs photo"><div role="img" aria-label="Photo of a man with a dog on a jetty by a lake at sunset"></div></div>
  <h1 class="abs venue-name">National Park</h1>
  <div class="abs rule" style="left:301px;top:284px;width:305px"></div>
  <div class="abs addr">Via Lentara 48<br>00194 Rome (RM)<br>Via Lentara, 48</div>
  <div class="abs directions">Get directions <span class="gtick">→</span></div>
  <div class="abs rule" style="left:301px;top:396px;width:305px"></div>
  <div class="abs venue-actions">Save venue<span class="mini-ico"></span>&nbsp;&nbsp;&nbsp;&nbsp;&nbsp;&nbsp;&nbsp; Email friends<span class="mini-ico"></span></div>

  <div class="abs description">
    <h3>Description</h3>
    We are Metro Calverton's premier multi-sports and entertainment complex located in Ashgrove Heights, MI. Offering both youth and adult leagues for softball, soccer, volleyball, basket-ball, golf, kickball and flag football.
  </div>

  <div class="abs events-table">
    <div class="bar-head" style="position:relative">National park events<span class="right">Add event <span class="gtick">+</span></span></div>
    <div class="cols"><span class="c" style="left:15px">Date:</span><span class="c" style="left:75px">Time:</span><span class="c" style="left:188px">Event:</span>
      <svg class="c" style="left:458px;top:6px" width="22" height="10" viewBox="0 0 22 10"><rect x="0" y="0" width="8" height="9" fill="none" stroke="#e2540d"/><rect x="0" y="0" width="8" height="2" fill="#e2540d"/><circle cx="13" cy="9" r="1.3" fill="#e2540d"/><path d="M12 5a4 4 0 0 1 4 4M12 1a8 8 0 0 1 8 8" fill="none" stroke="#e2540d" stroke-width="1.3"/></svg>
    </div>
    <div class="row first"><span class="c" style="left:15px">Monday 14</span><span class="c" style="left:75px">19:50 PM</span><span class="c" style="left:188px">Vantorra Band concert</span><span class="buy">BUY TICKET</span></div>
    <div class="row"><span class="c" style="left:15px">Monday 14</span><span class="c" style="left:75px">19:50 PM</span><span class="c" style="left:188px">Vantorra Band concert</span></div>
    <div class="row alt"><span class="c" style="left:15px">Monday 14</span><span class="c" style="left:75px">19:50 PM</span><span class="c" style="left:188px">Vantorra Band concert</span></div>
  </div>

  <div class="abs comments">
    <div class="bar-head">Circlepage comments</div>
    <div class="comment-box">
      <div class="avatar" role="img" aria-label="Commenter profile picture"></div>
      <div class="comment-input">Add a comment...</div>
      <div class="post-check"><i></i>Post to Circlepage</div>
      <div class="posting-as">Posting as Edvin Marlos <b>(Not you?)</b></div>
      <div class="comment-btn">Comment</div>
    </div>
  </div>
  <div class="abs rule" style="left:123px;top:778px;width:483px"></div>
  <div class="abs plugin"><i></i>Circlepage social plugin</div>

  <form class="abs newsletter">
    <p>Receive weekly event<br>list for <b>Roma</b></p>
    <div class="field">Enter your email here...</div>
    <div class="send">Sumbit</div>
  </form>
</main>

<aside>
  <div class="abs map-panel"><div class="map" role="img" aria-label="Street map of Rome with the venue pin"></div></div>
  <div class="abs ad" role="img" aria-label="Advertisement: green beer bottle on a bright green swirl background"></div>
</aside>

<footer class="abs site-footer">
  <div class="social">
    <span><i></i></span><span><i></i></span>
    <span><svg width="20" height="14" viewBox="0 0 20 14"><rect x="0" y="0" width="20" height="14" fill="#e8e8e8"/><path d="M0 0l10 8 10-8" fill="none" stroke="#222" stroke-width="1.6"/></svg></span>
    <span><i></i></span><span style="border:0"><i></i></span>
  </div>
  <div class="foot-rule" style="top:38px"></div>

  <div class="col" style="left:31px"><h4>Site pages</h4>Home<br>Events<br><span class="in">Event Map</span><br>Venues<br>Cinema<br><span class="in">Showtimes</span><br><span class="in">Trailers</span><br>Blog / News</div>
  <div class="vsep" style="left:118px"></div>
  <div class="col" style="left:134px"><h4>About Us</h4>About<br>Jobs<br>Advertise<br>Affiliate program<br>Contact Us</div>
  <div class="vsep" style="left:236px"></div>
  <div class="col" style="left:251px"><h4>Your account</h4>Log in / Register<br>Add Event +<br>Add Venue +</div>
  <div class="vsep" style="left:356px"></div>
  <div class="col" style="left:374px"><h4>Popular events</h4>Event1<br>Event2<br>Event3<br>Event4</div>
  <div class="vsep" style="left:487px"></div>
  <div class="col" style="left:503px"><h4>Popular categories</h4>Terms of Use<br>Privacy policy<br>Send us feedback</div>
  <div class="vsep" style="left:635px"></div>
  <div class="col" style="left:654px"><h4>Popular cinema</h4>Terms of Use<br>Terms of Use<br>Terms of Use</div>

  <div class="foot-rule" style="top:244px"></div>
  <p class="copyright">Pellora Copyright © 2012 Orvane Ventures, LLC. All rights reserved.<br>Use of this website signifies your agreement to the <b>Terms of Use</b> and <b>Online Privacy Policy</b></p>
</footer>

</body>
</html>
```